Business Card design for construction company

I would like a business card design for a construction company - Harlow Constructions. I have attached the ai logo file for use. I would like the card to be very smart and clean and incorporate only white and the two colours in the logo. I would like the card to have two sides. One side can just have the logo, the other with the relevant information.

Target Market(s)

Building and Construction Clients

Industry/Entity Type

Business

Contact Information for Business Card

Name: Tom Pardoe
Company: Harlow Constructions Pty Limited
Address: 14 Mallee Crescent Carrow Vale 2093
Phone: 0427 531 068
Email: tomp@harlowbuild-example.com.au

Font styles to use
Serif
Sans Serif

Requirements
Must have
• Details noted above
• Logo as provided
• Colours as in logo
• Square edges
• A font that compliments the logo
Should not have
• Any colour other than white and those in logo
• Rounded edges

```html
<!DOCTYPE html>
<html lang="en">
<head>
<meta charset="utf-8">
<title>Harlow Constructions – Business Card</title>
<link rel="stylesheet" href="https://fonts.googleapis.com/css2?family=Open+Sans:wght@400;700&display=swap">
<style>
  :root {
    --backdrop: #e6e7e9;
    --card-white: #ffffff;
    --card-dark: #2c2c2e;
    --card-dark-edge: #3a3a3d;
    --ink-dark: #3a3a3c;
    --ink-light: #ffffff;
    --accent-blue: #2aa7df;
    --faint-on-white: #ececee;
    --faint-on-dark: #38383b;
  }
  * { margin: 0; padding: 0; box-sizing: border-box; }
  html, body {
    width: 1200px; height: 800px; overflow: hidden;
    background: var(--backdrop);
    font-family: "Open Sans", Arial, sans-serif;
  }
  .stage {
    position: relative; width: 1200px; height: 800px;
    display: flex; align-items: center; justify-content: center; gap: 60px;
  }
  .card {
    position: relative; width: 500px; height: 286px; overflow: hidden;
    box-shadow: 0 10px 30px rgba(0,0,0,0.12);
  }
  .card--front { background: var(--card-white); }
  .card--back { background: linear-gradient(135deg, var(--card-dark-edge), var(--card-dark) 60%); }

  .wordmark {
    position: absolute; display: flex; align-items: center; gap: 10px;
    font-weight: 400; letter-spacing: 3px; text-transform: uppercase; white-space: nowrap;
  }
  .wordmark__square { width: 10px; height: 10px; background: var(--accent-blue); flex: none; }
  .card--front .wordmark { left: 48px; top: 66px; font-size: 21px; color: var(--ink-dark); }
  .card--back .wordmark { left: 150px; top: 40px; font-size: 19px; color: var(--ink-light); }

  .watermark-name {
    position: absolute; font-weight: 700; text-transform: uppercase;
    font-size: 78px; line-height: 1; letter-spacing: 4px; white-space: nowrap;
    writing-mode: vertical-rl;
  }
  .card--front .watermark-name { right: -6px; top: 20px; color: var(--faint-on-white); transform: rotate(180deg); }
  .card--back .watermark-name { left: -8px; top: -10px; color: var(--faint-on-dark); transform: rotate(180deg); }

  .holder { position: absolute; left: 220px; top: 108px; color: var(--ink-light); }
  .holder__name { font-size: 14px; font-weight: 700; text-transform: uppercase; letter-spacing: .3px; }
  .holder__company { font-size: 12px; font-weight: 700; margin-top: 1px; }

  .contact-list { position: absolute; left: 150px; top: 172px; list-style: none; color: var(--ink-light); }
  .contact-list li {
    display: flex; align-items: center; gap: 8px;
    font-size: 12.5px; font-weight: 700; line-height: 22px;
  }
  .contact-icon { width: 14px; height: 14px; flex: none; }
</style>
</head>
<body>
<main class="stage">
  <section class="card card--front" aria-label="Card front">
    <div class="watermark-name" aria-hidden="true">Harlow</div>
    <div class="wordmark"><span class="wordmark__square"></span>Harlow Constructions</div>
  </section>

  <section class="card card--back" aria-label="Card back">
    <div class="watermark-name" aria-hidden="true">Harlow</div>
    <div class="wordmark"><span class="wordmark__square"></span>Harlow Constructions</div>
    <div class="holder">
      <p class="holder__name">Tom Pardoe</p>
      <p class="holder__company">Harlow Constructions Pty Limited</p>
    </div>
    <ul class="contact-list">
      <li>
        <svg class="contact-icon" viewBox="0 0 14 14" aria-hidden="true"><circle cx="7" cy="7" r="7" fill="#fff"/><path d="M7 3.2a2.3 2.3 0 0 0-2.3 2.3C4.7 7.3 7 10.6 7 10.6s2.3-3.3 2.3-5.1A2.3 2.3 0 0 0 7 3.2zm0 3.2a.9.9 0 1 1 0-1.8.9.9 0 0 1 0 1.8z" fill="#2c2c2e"/></svg>
        14 Mallee Crescent Carrow Vale 2093
      </li>
      <li>
        <svg class="contact-icon" viewBox="0 0 14 14" aria-hidden="true"><circle cx="7" cy="7" r="7" fill="#fff"/><path d="M5 3.6l1.1 1.7-.7.8c.4.9 1.1 1.6 2 2l.8-.7 1.7 1.1-.5 1.2c-2.6-.2-4.7-2.3-4.9-4.9z" fill="#2c2c2e"/></svg>
        0427 531 068
      </li>
      <li>
        <svg class="contact-icon" viewBox="0 0 14 14" aria-hidden="true"><circle cx="7" cy="7" r="7" fill="#fff"/><rect x="3.5" y="4.5" width="7" height="5" fill="none" stroke="#2c2c2e" stroke-width="1"/><path d="M3.5 4.5 7 7.3l3.5-2.8" fill="none" stroke="#2c2c2e" stroke-width="1"/></svg>
        tomp@harlowbuild-example.com.au
      </li>
    </ul>
  </section>
</main>
</body>
</html>
```